Coaching landingpage/salespage need a layout

Hi!
We are two people from Sweden looking for help to design our coaching landingpage/salespage.

What about:
We need a nice modern timeless appealing Photoshop layout (landingpage) for our coaching page where we coach people to “how to get a richer lifestyle”.

Style of page:
We want the site to reflect seriousness but still harmonic. We would like somewhat colorful and (but not too crazy). After all, we are coaching about investments and private economy.
Responsive layout – consider stacking order when scaling down window width. Fullpage-design where content areas are 960 grid/max-width.

----------------------------------------------------------------------------
Content on page:
*Headersection – Logo and header image with the two coaches together and space for later on adding a video.

*On the landingpage the customers can read up on what we mean by a richer lifestyle (use dummy text). We show our Trivselsnyckeln (= Lifestyle matrix) and a little description about that. If the customers want to know more, they can click "read more (or a symbolic icon that relates to read more)" to expand a hidden div (section) where they can read more about Trivselsnyckeln. They can also minimize the section.

*3-4 Unique selling points “Four reasons why choose coaching” with nice designed number-icons and some place for text.

*The customer should also be able to read something about what happens during a typical coaching session, some bullets that summarize it (use dummy text) and a couple of headlines, maybe 3 or 4 (about what they need to prepare for themselves .eg Callwave, headset/microphone etc).

*Offer/product section: A section where the customer can see what services we provide, choose product and click order. When customer click order they will arrive to an order-page (this one you don’t have to design) .
Our products are as followed: Bronze (single coaching session), Silver (small-package), Gold (large-package). Use provided graphics for these products.

*Testimonials section. Currently we have 2 good testimonials, but only with text no portrait picture.

Testimonial1: “Uppiggande och inspirerande! Kommer med enkla vardagstips såväl som svårare tips. Ett roligt sätt att få en spark i baken, så att ekonomi-energin bibehålls! Tack för ett bra samtal!" - Josefin Brandeby

Testimonial2: "Värdefullast för mig var kunskapen om alternativa investeringssställen som inte är börs eller eget ägande." - Annika Sjöhalla

*Section with portraits and info about the coaches (currently 2 coaches, but in future will be several, so a design-section that’s lets us add more coaches).

*Footer-section
------------------------------------------------------------------------

Colors:
Use Trivselsnyckeln (attached file) as colorinspiration. Doesn’t have to be exactly those colors, you can use similar colors if it is more pleasing to the eye and you can also use complementary colors.

Currently we have tried of our own but don't really nail it with any apealing design. This is what we have done so far but we want to replace it with your more professional design:

https://www.harbekrona.se/full/Page/coaching13
-------------------------------------------------------------

SUMMARIZE of the above design-description:

* Our logo (attached psd-file with smart-object. You can try different colors with color-overlay)

*Apealing headerimage with portrait (attached file "big_portrait")

*Introduction text (use dummy text about 100 words)

*Text about Trivselsnyckeln (use dummy text about 200 words)

*Trivselsnyckeln (attached psd-file with smart-object)

*What we are covering during a coaching session (dummy text about 200 words and about 5 or 6 bullets)

*3-4 Unique Selling Points with stylish number icons (not 2 small) and some text.
*Our offers Bronze, Silver, Gold (attached pictures)
*Testimonials
*Picture & info about coaches (attached pictures, choose whichever suits you)
*Footer

Please comment if there are questions.

Reagards Torbjörn @ Harbe Krona

Target Market(s)

People who want to learn how to create a richer lifestyle which involves more freedom and a better well-being

Number of Pages Required

1 page

Font styles to use
Sans Serif
Other font styles liked:
• Roboto

Requirements
Should not have
• A cheezy unmodern landingpage with lots of texts and 10 sign-up buttons.
• This page is not a site about capturing emails and building lists by provide a "best-guide-for-something". It´s about getting people to book and pay for one or more coaching-sessions.

```html
<!DOCTYPE html>
<html lang="en">
<head>
<meta charset="utf-8">
<title>Harbe Krona – Lifestyle Coaching</title>
<link rel="stylesheet" href="https://fonts.googleapis.com/css2?family=Open+Sans:wght@400;600;700&family=Roboto:wght@400;500;700&display=swap">
<style>
:root{
  --orange:#f6a524;
  --orange-dark:#e48f12;
  --ink:#2f2f2f;
  --text:#7d7d7d;
  --muted:#a3a3a3;
  --light:#efefef;
  --panel:#d9d9d9;
  --blue:#1d9ad6;
  --taupe:#8b786a;
  --silver:#a9a9a9;
  --gold:#d9a91c;
  --footer:#3b3b3b;
  --footer-deep:#2c2c2c;
  --white:#ffffff;
}
*{box-sizing:border-box;margin:0;padding:0}
html,body{width:1200px;height:3797px;overflow:hidden}
body{font-family:"Open Sans",Arial,sans-serif;color:var(--text);background:var(--white);font-size:13px;line-height:1.6}
.wrap{width:786px;margin:0 auto;position:relative}
h2.section-title{font-family:"Roboto",Arial,sans-serif;font-weight:700;color:var(--ink);font-size:24px;text-align:center}
.rule{width:50px;height:2px;background:var(--orange);margin:10px auto 0}
.btn{display:inline-block;background:var(--orange);color:var(--white);font-size:11px;padding:7px 18px;border-radius:2px;text-decoration:none}
.mark{width:22px;height:22px;background:var(--orange);margin:0 auto 14px}

/* Header */
.site-header{height:81px;background:var(--orange)}
.site-header .wrap{display:flex;align-items:center;justify-content:space-between;height:81px}
.brand{display:flex;align-items:center;gap:10px;color:var(--white);font-family:"Roboto",sans-serif;font-size:26px;font-weight:400;letter-spacing:1px}
.brand-square{width:26px;height:26px;background:var(--white)}
.main-nav{display:flex;gap:4px}
.main-nav a{color:var(--white);font-size:13px;font-weight:600;text-decoration:none;padding:8px 10px}
.main-nav a.active{background:var(--white);color:var(--ink);border-bottom:3px solid var(--ink)}

/* Hero */
.hero{height:329px;background:radial-gradient(ellipse at 70% 50%,#8c8c8c 0%,#5e5e5e 55%,#474747 100%);position:relative;overflow:hidden}
.hero .wrap{height:329px}
.hero-copy{position:absolute;left:0;top:60px;width:320px;color:var(--white);z-index:2}
.hero-copy h1{font-family:"Roboto",sans-serif;font-size:25px;font-weight:700;line-height:1.3;margin-bottom:16px}
.hero-copy p{font-size:11.5px;font-weight:600;line-height:1.6;margin-bottom:22px}
.btn-outline{display:inline-block;border:2px solid var(--orange);color:var(--orange);font-size:12px;padding:8px 22px;text-decoration:none}
.hero-photo{position:absolute;left:350px;top:26px;width:490px;height:303px;z-index:1;background:linear-gradient(180deg,#9a9a9a 0%,#6f6f6f 60%,#4b4b4b 100%)}

/* Intro */
.intro{height:405px;text-align:center;padding-top:48px}
.intro p{width:650px;margin:18px auto 20px;font-size:12px;line-height:1.7}

/* Matrix */
.matrix{height:410px;background:var(--light)}
.matrix .wrap{display:flex;align-items:center;height:410px;gap:60px}
.matrix-figure{width:240px;height:290px;margin-left:70px;background:linear-gradient(135deg,#4ab0e3 0%,#f3b53a 35%,#9a8270 65%,#48b96b 100%);opacity:.85}
.matrix-text{width:400px}
.matrix-text h3{font-family:"Roboto",sans-serif;color:var(--ink);font-size:21px;font-weight:700}
.matrix-text .rule{margin:8px 0 16px}
.matrix-text p{font-size:12px;margin-bottom:18px}

/* Reasons */
.reasons{height:332px;padding-top:40px}
.reason-grid{display:flex;justify-content:space-between;margin-top:32px}
.reason{width:178px;height:190px;background:var(--white);box-shadow:0 0 0 1px #ececec;text-align:center}
.reason-head{height:56px;background:#f2f2f2;color:var(--blue);font-family:"Roboto",sans-serif;font-weight:700;font-size:17px;padding-top:8px}
.reason.featured .reason-head{background:var(--orange);color:var(--white)}
.reason-num{width:76px;height:76px;border-radius:50%;background:var(--blue);color:var(--white);font-family:"Roboto",sans-serif;font-size:34px;line-height:70px;margin:-22px auto 10px;border:4px solid var(--white)}
.reason.featured .reason-num{background:var(--taupe)}
.reason p{font-size:10.5px;line-height:1.45;padding:0 16px}

/* Session */
.session{height:532px;padding-top:26px}
.session h4{font-family:"Roboto",sans-serif;color:var(--ink);font-size:16px;font-weight:700;margin:28px 0 10px;opacity:.8}
.session p{font-size:11px;line-height:1.6}
.session .lead-in{color:var(--ink);font-weight:700;margin-top:10px}
.checklist{list-style:none;margin-top:8px}
.checklist li{font-size:11px;line-height:1.6;display:flex;gap:6px;align-items:center}
.checklist svg{flex:none}
.session-cols{display:flex;justify-content:space-between}
.session-cols>div{width:370px}
.session-cols h4{margin-top:16px}

/* Packages */
.packages{height:570px;background:var(--light);padding-top:40px;text-align:center}
.packages .intro-text{width:650px;margin:18px auto 0;font-size:12px}
.package-grid{display:flex;justify-content:space-between;margin-top:40px}
.package{width:240px;height:342px;background:var(--white);border:1px solid #e2e2e2;position:relative;padding-top:170px}
.package-top{position:absolute;top:0;left:0;right:0;height:220px;background:#f7c98c}
.package.silver .package-top{background:#d8d8d8}
.package.gold .package-top{background:#f4d67a}
.medal{position:absolute;left:50%;top:-20px;margin-left:-78px;width:156px;height:156px;border-radius:50%;border:8px solid var(--white);box-shadow:0 2px 6px rgba(0,0,0,.2)}
.bronze .medal{background:radial-gradient(circle at 40% 35%,#e9a06a,#b2602c 70%)}
.silver .medal{background:radial-gradient(circle at 40% 35%,#f4f4f4,#a8a8a8 70%)}
.gold .medal{background:radial-gradient(circle at 40% 35%,#f7dc72,#c49214 70%)}
.package-label{position:relative;height:46px;line-height:46px;color:var(--white);font-family:"Roboto",sans-serif;font-weight:700;font-size:17px;background:var(--orange-dark)}
.silver .package-label{background:var(--silver)}
.gold .package-label{background:var(--gold)}
.package-body{padding-top:16px;font-size:11px;line-height:1.5}
.btn-ghost{display:inline-block;margin-top:22px;border:1px solid #cfcfcf;color:var(--text);font-size:10px;padding:6px 22px;text-decoration:none}

/* Testimonials */
.testimonials{height:341px;padding-top:40px;text-align:center}
.testimonials blockquote{width:560px;margin:34px auto 0;font-size:12px;line-height:1.6}
.testimonials cite{display:block;font-style:normal;font-weight:700;color:var(--ink);font-size:13px;margin-top:20px}
.dots{display:flex;justify-content:center;gap:6px;margin-top:12px}
.dots span{width:8px;height:8px;border-radius:50%;background:#bdbdbd}
.dots span.on{background:var(--blue)}

/* Coaches */
.coaches{height:481px;background:var(--light);padding-top:40px}
.coach-grid{display:flex;justify-content:space-between;margin-top:64px}
.coach{width:370px;height:330px;background:var(--panel);text-align:center;position:relative;padding-top:100px}
.coach-photo{position:absolute;left:50%;top:-44px;margin-left:-62px;width:124px;height:124px;border-radius:50%;border:5px solid var(--white);background:linear-gradient(180deg,#b9b9b9,#7d7d7d)}
.coach h3{font-family:"Roboto",sans-serif;color:var(--ink);font-size:18px;font-weight:500}
.coach .mail{color:var(--orange-dark);font-size:10.5px;text-decoration:underline}
.coach p{font-size:10.5px;line-height:1.55;padding:18px 40px 0}
.slider-arrow{position:absolute;top:255px;color:#b3b3b3}
.slider-arrow.prev{left:-62px}
.slider-arrow.next{right:-62px}

/* Footer */
.site-footer{height:292px;background:var(--footer);color:#cfcfcf;padding-top:44px}
.site-footer .wrap{display:flex}
.footer-brand{width:370px}
.footer-brand .brand{font-size:24px;margin-bottom:22px}
.footer-line{display:flex;gap:12px;font-size:11.5px;line-height:1.5;margin-bottom:18px}
.footer-line a{color:var(--orange);text-decoration:underline}
.footer-links{width:186px}
.footer-links h5,.footer-follow h5{color:var(--white);font-size:13px;font-weight:600;margin-bottom:18px}
.footer-links ul{list-style:none;font-size:11.5px;line-height:2.5}
.footer-links li:first-child{color:var(--orange);text-decoration:underline}
.social-box{width:150px;height:100px;background:#e4e4e4;border:3px solid #fff}
.copyright{height:24px;background:var(--footer-deep);color:#a5a5a5;font-size:10px;text-align:center;line-height:24px}
</style>
</head>
<body>

<header class="site-header">
  <div class="wrap">
    <div class="brand"><span class="brand-square"></span>HARBE KRONA</div>
    <nav class="main-nav">
      <a class="active" href="#">Home</a>
      <a href="#">About Us</a>
      <a href="#">Packages</a>
      <a href="#">Coaches</a>
      <a href="#">Testimonials</a>
      <a href="#">Contact Us</a>
    </nav>
  </div>
</header>

<section class="hero">
  <div class="wrap">
    <div class="hero-copy">
      <h1>Lorem Ipsum has been the dard dummy text.</h1>
      <p>with the release of Typeset sheets containing Lorem Ipsum passages, and more recently with desktop publishing software like Folio Layout.</p>
      <a class="btn-outline" href="#">Book Now</a>
    </div>
    <div class="hero-photo" role="img" aria-label="Portrait photo of the two coaches standing together"></div>
  </div>
</section>

<section class="intro">
  <div class="wrap">
    <div class="mark"></div>
    <h2 class="section-title">One Step That Can Change Your Life</h2>
    <p>Lifestyle Coaching is about finding out what creates a highly prosperous and high freedom in your life. It's about finding out what you really want with your life and then step by step to design a lifestyle around all this. A lifestyle that will last a lifetime and not...</p>
    <a class="btn" href="#">Read More</a>
  </div>
</section>

<section class="matrix">
  <div class="wrap">
    <div class="matrix-figure" role="img" aria-label="Trivselsnyckeln lifestyle matrix with four coloured quadrants"></div>
    <div class="matrix-text">
      <h3>What is a richer lifestyle?</h3>
      <div class="rule"></div>
      <p>What is a richer lifestyle may differ between different people. It can also be quite difficult on their own to get a good picture of what you really mean by this. We have therefore developed a simple model to facilitate the understanding...</p>
      <a class="btn" href="#">Read More</a>
    </div>
  </div>
</section>

<section class="reasons">
  <div class="wrap">
    <h2 class="section-title">Why Choose Coaching?</h2>
    <div class="reason-grid">
      <div class="reason"><div class="reason-head">Commitment</div><div class="reason-num">01</div><p>Everyone can set goals, but not everyone has the ability to pursue.</p></div>
      <div class="reason featured"><div class="reason-head">Challenging</div><div class="reason-num">02</div><p>We will help you to get outside your comfort zone. It is outside the...</p></div>
      <div class="reason"><div class="reason-head">Support</div><div class="reason-num">03</div><p>All we sometimes need support, especially in the quest to create...</p></div>
      <div class="reason"><div class="reason-head">You are unique</div><div class="reason-num">04</div><p>There is no 'one-fits-all' solution. Everyone is different with...</p></div>
    </div>
  </div>
</section>

<section class="session">
  <div class="wrap">
    <h2 class="section-title">We Are Covering Coaching Session</h2>
    <h4>How does it work?</h4>
    <p>Together with your coach you will develop a tailored approach that is appropriate for your circumstances and ambitions. This is because we humans are in different phases of life. Some need more time to find out what they really want to live the lifestyle while others have different obstacles in their path they need to address in order to achieve the results they want. There are many areas to focus on, depending on where you are in life.</p>
    <p class="lead-in">These are examples of different areas that your coach will go through with you.</p>
    <ul class="checklist">
      <li><svg width="10" height="10" viewBox="0 0 10 10"><rect width="10" height="10" fill="#8a8a8a"/><path d="M2 5l2 2 4-4" stroke="#fff" stroke-width="1.5" fill="none"/></svg>Where are you right now in the life-style array?</li>
      <li><svg width="10" height="10" viewBox="0 0 10 10"><rect width="10" height="10" fill="#8a8a8a"/><path d="M2 5l2 2 4-4" stroke="#fff" stroke-width="1.5" fill="none"/></svg>Where do you want to be in the life-style array?</li>
      <li><svg width="10" height="10" viewBox="0 0 10 10"><rect width="10" height="10" fill="#8a8a8a"/><path d="M2 5l2 2 4-4" stroke="#fff" stroke-width="1.5" fill="none"/></svg>Find a niche that suits you and your desire to live in fun</li>
      <li><svg width="10" height="10" viewBox="0 0 10 10"><rect width="10" height="10" fill="#8a8a8a"/><path d="M2 5l2 2 4-4" stroke="#fff" stroke-width="1.5" fill="none"/></svg>Getting Started, or build your own money machine</li>
      <li><svg width="10" height="10" viewBox="0 0 10 10"><rect width="10" height="10" fill="#8a8a8a"/><path d="M2 5l2 2 4-4" stroke="#fff" stroke-width="1.5" fill="none"/></svg>Break down big goals into manageable sub-goals</li>
      <li><svg width="10" height="10" viewBox="0 0 10 10"><rect width="10" height="10" fill="#8a8a8a"/><path d="M2 5l2 2 4-4" stroke="#fff" stroke-width="1.5" fill="none"/></svg>Continuously check that you are on track and making progress</li>
    </ul>
    <div class="session-cols">
      <div>
        <h4>What do I need?</h4>
        <p>The call is implemented via the program Callwave. All you need is a computer and a headset, alternatively, a microphone and speakers.</p>
      </div>
      <div>
        <h4>How do I book coaching?</h4>
        <p>Select a single session or one of our packages. Write what times of day that suits you best. We will contact you then to find a time that suits us both.</p>
      </div>
    </div>
  </div>
</section>

<section class="packages">
  <div class="wrap">
    <h2 class="section-title">Invest in Your Self</h2>
    <div class="rule"></div>
    <p class="intro-text">You want something you do not already have? Start when designing a lifestyle you have not previously lived. We, at Harbe Krona will help you with this by lifestyle coaching. Below, you can choose one of our coaching packages.</p>
    <div class="package-grid">
      <div class="package bronze">
        <div class="package-top"></div>
        <div class="medal" role="img" aria-label="Bronze package medallion"></div>
        <div class="package-label">Disposable Session</div>
        <div class="package-body">Includes 1 session<br>Price 650 SEK<br><a class="btn-ghost" href="#">Book Now</a></div>
      </div>
      <div class="package silver">
        <div class="package-top"></div>
        <div class="medal" role="img" aria-label="Silver package medallion"></div>
        <div class="package-label">Silver Package</div>
        <div class="package-body">Includes 5 sessions<br>Price 3050 SEK<br><a class="btn-ghost" href="#">Book Now</a></div>
      </div>
      <div class="package gold">
        <div class="package-top"></div>
        <div class="medal" role="img" aria-label="Gold package medallion"></div>
        <div class="package-label">Gold Package</div>
        <div class="package-body">Includes 10 sessions<br>Price 5800 SEK<br><a class="btn-ghost" href="#">Book Now</a></div>
      </div>
    </div>
  </div>
</section>

<section class="testimonials">
  <div class="wrap">
    <h2 class="section-title">Testimonials</h2>
    <div class="rule"></div>
    <blockquote>Refreshing and inspiring! Comes with simple everyday tips as well as harder tips. A fun way to get a kick in the butt, so that the economy-energy is maintained! Thanks for a good conversation
      <cite>Josefin Brandeby</cite>
    </blockquote>
    <div class="dots"><span class="on"></span><span></span></div>
  </div>
</section>

<section class="coaches">
  <div class="wrap">
    <h2 class="section-title">We As Coaches</h2>
    <div class="rule"></div>
    <div class="coach-grid">
      <article class="coach">
        <div class="coach-photo" role="img" aria-label="Portrait photo of coach Torbjörn Lindqvist"></div>
        <h3>Torbjörn Lindqvist</h3>
        <a class="mail" href="#">torbjorn@harbekrona.se</a>
        <p>Versatile investors with a focus on alternative and high-risk investments. Besides the stock market, investing in unlisted startup companies and various internet based investments such as P2P lending, online games and apps.</p>
      </article>
      <article class="coach">
        <div class="coach-photo" role="img" aria-label="Portrait photo of coach Mattias Lönnberg"></div>
        <h3>Mattias Lönnberg</h3>
        <a class="mail" href="#">mattias@harbekrona.se</a>
        <p>Mattias has a broad background in finance and IT. As an investor he focuses on dividend stocks, real estate and internet-based entrepreneurship. He also has a long experience and a passion to help people and businesses to evolve in different ways, creating more good days in life.</p>
      </article>
    </div>
    <svg class="slider-arrow prev" width="20" height="36" viewBox="0 0 20 36"><path d="M16 2L4 18l12 16" stroke="currentColor" stroke-width="2" fill="none"/></svg>
    <svg class="slider-arrow next" width="20" height="36" viewBox="0 0 20 36"><path d="M4 2l12 16L4 34" stroke="currentColor" stroke-width="2" fill="none"/></svg>
  </div>
</section>

<footer class="site-footer">
  <div class="wrap">
    <div class="footer-brand">
      <div class="brand"><span class="brand-square"></span>HARBE KRONA</div>
      <div class="footer-line">
        <svg width="16" height="22" viewBox="0 0 16 22"><path d="M8 1a7 7 0 0 0-7 7c0 5 7 13 7 13s7-8 7-13a7 7 0 0 0-7-7z" fill="#1d9ad6"/><circle cx="8" cy="8" r="2.6" fill="#3b3b3b"/></svg>
        <span>Harbe Krona AB Lindvägen 12<br>2A Göteborg</span>
      </div>
      <div class="footer-line">
        <svg width="16" height="22" viewBox="0 0 16 22"><text x="3" y="17" font-family="Open Sans,sans-serif" font-size="18" font-weight="700" fill="#1d9ad6">?</text></svg>
        <span>For Questions, Contact Us At<br><a href="#">team@harbekrona.se</a></span>
      </div>
    </div>
    <div class="footer-links">
      <h5>Quick Links</h5>
      <ul><li>• Blogg</li><li>• Coaching</li><li>• Om oss</li></ul>
    </div>
    <div class="footer-follow">
      <h5>Follow Us on Socialhub</h5>
      <div class="social-box" role="img" aria-label="Social page preview widget"></div>
    </div>
  </div>
</footer>
<div class="copyright">Copyright 2016 Harbe Krona AB</div>

</body>
</html>
```